SEHLAN REAL ESTATE
شركة السهلان العقارية
Creative Brief
Simple
FAISAL ALQUDRANI
Real Estate Consultant & Developer
SAUDI ARABIA.JEDDAH
f_alqudrani@mailvesta.com
THE LOGO
Yasahiro17 Yasahiro17
YADESIGN YADESIGN

```html
<!DOCTYPE html>
<html lang="en">
<head>
<meta charset="utf-8">
<title>Sehlan Real Estate – Business Card</title>
<link rel="stylesheet" href="https://fonts.googleapis.com/css2?family=Cinzel:wght@400;600&family=Tinos:wght@700&family=Noto+Naskh+Arabic:wght@500&display=swap">
<style>
  :root {
    --page: #ffffff;
    --card: #ffffff;
    --card-edge: #c9c9c9;
    --brand-blue: #3a8ee6;
    --ink: #111111;
    --white: #ffffff;
    --photo-sky: #7fa3c4;
    --photo-house: #d9d4cb;
    --photo-ground: #3d4a3a;
  }
  * { box-sizing: border-box; margin: 0; padding: 0; }
  html, body { width: 1200px; height: 1057px; overflow: hidden; background: var(--page); }
  .sheet { position: relative; width: 1200px; height: 1057px; }

  .side-label {
    position: absolute; top: 62px; width: 528px; text-align: center;
    font-family: "Tinos", "Times New Roman", serif; font-weight: 700;
    font-size: 62px; color: var(--ink);
  }
  .side-label--front { left: 72px; }
  .side-label--back { left: 636px; }

  .card {
    position: absolute; top: 150px; width: 528px; height: 895px;
    background: var(--card); border: 1.5px solid var(--card-edge); overflow: hidden;
  }
  .card--front { left: 72px; }
  .card--back { left: 636px; }

  .card__photo {
    position: absolute; left: 0; top: 0; width: 100%; height: 440px;
    background: linear-gradient(180deg, var(--photo-sky) 0%, #a9bfd2 35%, var(--photo-house) 60%, #8c8a80 82%, var(--photo-ground) 100%);
  }

  .card__band {
    position: absolute; left: 0; top: 440px; width: 100%; height: 310px;
    background: var(--brand-blue); color: var(--white);
    font-family: "Cinzel", Georgia, serif; padding: 20px 0 0 30px;
  }
  .holder__first { font-size: 58px; font-weight: 400; line-height: 1; letter-spacing: 1px; }
  .holder__last { font-size: 34px; font-weight: 400; line-height: 1.15; letter-spacing: 1px; }
  .holder__role { font-size: 16.5px; font-weight: 600; margin-top: 2px; letter-spacing: .3px; }

  .contact-list { list-style: none; margin-top: 26px; }
  .contact-list li {
    display: flex; align-items: center; gap: 18px; height: 40px;
    font-size: 13px; font-weight: 600; letter-spacing: .2px;
  }
  .contact-list li.email { text-transform: none; font-family: "Tinos", serif; font-weight: 700; font-size: 13px; }
  .contact-icon { width: 24px; height: 24px; flex: none; }

  .brand {
    position: absolute; left: 0; width: 100%;
    display: flex; align-items: center; justify-content: center; gap: 12px;
    color: var(--brand-blue);
  }
  .brand--front { top: 782px; }
  .brand--back { top: 412px; }
  .brand__mark { width: 40px; height: 40px; background: var(--brand-blue); }
  .brand__text { display: flex; flex-direction: column; align-items: flex-start; line-height: 1.15; font-weight: 600; }
  .brand__name { font-family: "Cinzel", Georgia, serif; font-size: 22px; letter-spacing: .5px; }
  .brand__name-ar { font-family: "Noto Naskh Arabic", serif; font-size: 20px; font-weight: 500; direction: rtl; }

  .recycle { position: absolute; right: 26px; bottom: 20px; width: 36px; height: 36px; }
</style>
</head>
<body>
<main class="sheet">
  <h2 class="side-label side-label--front">Front</h2>
  <h2 class="side-label side-label--back">Back</h2>

  <section class="card card--front">
    <div class="card__photo" role="img" aria-label="Photograph of a modern white two-storey villa with glass balconies at dusk"></div>

    <div class="card__band">
      <h1 class="holder">
        <span class="holder__first" style="display:block">FAISAL</span>
        <span class="holder__last" style="display:block">ALQUDRANI</span>
      </h1>
      <p class="holder__role">REAL ESTATE CONSULTANT &amp; DEVELOPER</p>

      <ul class="contact-list">
        <li>
          <svg class="contact-icon" viewBox="0 0 24 24" fill="none" stroke="#fff" stroke-width="1.5">
            <circle cx="12" cy="12" r="10.5"/>
            <path d="M8.5 7.5l1.8-.5 1 2.4-1.2.9a6 6 0 0 0 2.6 2.6l.9-1.2 2.4 1-.5 1.8c-3.8.4-7.4-3.2-7-7z" fill="#fff" stroke="none"/>
          </svg>
          <span>+966512340078</span>
        </li>
        <li>
          <svg class="contact-icon" viewBox="0 0 24 24" fill="none" stroke="#fff" stroke-width="1.5">
            <circle cx="12" cy="12" r="10.5"/>
            <path d="M12 18s-4-4.2-4-7a4 4 0 0 1 8 0c0 2.8-4 7-4 7z"/>
            <circle cx="12" cy="11" r="1.3" fill="#fff" stroke="none"/>
          </svg>
          <span>SAUDI ARABIA.JEDDAH</span>
        </li>
        <li class="email">
          <svg class="contact-icon" viewBox="0 0 24 24" fill="none" stroke="#fff" stroke-width="1.5">
            <circle cx="12" cy="12" r="10.5"/>
            <rect x="7" y="8.5" width="10" height="7" rx=".5"/>
            <path d="M7 9l5 3.5L17 9"/>
          </svg>
          <span>f_alqudrani@mailvesta.com</span>
        </li>
      </ul>
    </div>

    <div class="brand brand--front">
      <span class="brand__mark"></span>
      <div class="brand__text">
        <span class="brand__name">SEHLAN REAL ESTATE</span>
        <span class="brand__name-ar">شركة السهلان العقارية</span>
      </div>
    </div>
  </section>

  <section class="card card--back">
    <div class="brand brand--back">
      <span class="brand__mark"></span>
      <div class="brand__text">
        <span class="brand__name">SEHLAN REAL ESTATE</span>
        <span class="brand__name-ar">شركة السهلان العقارية</span>
      </div>
    </div>

    <svg class="recycle" viewBox="0 0 36 36" fill="#222">
      <path d="M15 4h6l4 7 3-1.7-2.5 7.2-7.4-1.4 3-1.7L18 8.5l-3.5 6-4-2.4z"/>
      <path d="M29 20l3 5.2-3 5.3h-8v3.4l-5-5.7 5-5.7v3.4h6.5l-3.4-5.9z"/>
      <path d="M12 31.5H6L3 26.3l4-7-3-1.7 7.4-1.4 2.5 7.2-3-1.8-3.3 5.8h4.4z"/>
    </svg>
  </section>
</main>
</body>
</html>
```